Leadership Development Company would like a design that represents our Company's Purpose, Vision &am

We have recently created our Purpose, Vision and Mission statements for our company and would like a visual representation that we can hang in our office.

We have a strong design in mind and have provided a diagram of what we believe would work for us. We would really like a designer to create a visual representation of these documents so that we can have them made into canvas art and placed in our office.

Target Market(s)

Internal Staff and Key Business Clients

Industry/Entity Type

Education

Requirements
Must have
• One design that is separated into three (3) different sections (Purpose + Vision + Mission)
• Corporate colours
• Correct dimensions (as per the attached brief)
• Be in Photoshop (PSD) format

```html
<!DOCTYPE html>
<html lang="en">
<head>
<meta charset="UTF-8">
<title>Vision · Purpose · Mission</title>
<link href="https://fonts.googleapis.com/css2?family=Bebas+Neue&display=swap" rel="stylesheet">
<style>
  :root {
    --sky-top: #7f93b4;
    --sky-mid: #9fb0c8;
    --horizon: #5e6f88;
    --ground: #a7b3c4;
    --ground-low: #6f7c8f;
    --base: #2b2f36;
    --ink: #ffffff;
    --icon-fill: #5b6b8c;
    --echo: rgba(255, 255, 255, 0.55);
  }
  * { margin: 0; padding: 0; box-sizing: border-box; }
  html, body { width: 1200px; height: 900px; overflow: hidden; }
  body { font-family: "Bebas Neue", "Oswald", sans-serif; color: var(--ink); }

  .canvas { position: relative; width: 1200px; height: 900px; overflow: hidden; }

  .landscape {
    position: absolute; inset: 0;
    background:
      linear-gradient(180deg,
        var(--sky-top) 0%,
        var(--sky-mid) 18%,
        #8797b0 30%,
        var(--horizon) 40%,
        #4f5f74 46%,
        var(--ground) 52%,
        #94a1b3 68%,
        var(--ground-low) 86%,
        var(--base) 100%);
  }

  .echo {
    position: absolute; font-size: 150px; line-height: 1;
    color: var(--echo); filter: blur(6px); letter-spacing: 2px;
  }
  .echo--vision { left: 48px; top: 222px; }
  .echo--purpose { left: 416px; top: 208px; }
  .echo--mission { left: 852px; top: 190px; font-size: 130px; }

  .title {
    position: absolute; font-size: 82px; line-height: 1;
    text-shadow: 0 2px 4px rgba(0,0,0,0.35);
  }
  .title--vision { left: 164px; top: 182px; }
  .title--purpose { left: 434px; top: 192px; }
  .title--mission { left: 836px; top: 162px; }

  .statement {
    position: absolute; text-align: center; font-size: 23px;
    line-height: 23.4px; text-shadow: 0 1px 3px rgba(0,0,0,0.45);
  }
  .statement--vision { left: 23px; width: 300px; top: 328px; }
  .statement--purpose { left: 440px; width: 290px; top: 340px; }
  .statement--mission { left: 820px; width: 360px; top: 277px; font-size: 21.5px; line-height: 21.6px; }
  .statement--mission p + p { margin-top: 21px; }

  .icon { position: absolute; }
  .icon--eye { left: 34px; top: 74px; width: 222px; height: 102px; }
  .icon--heart { left: 614px; top: 80px; width: 168px; height: 138px; }
  .icon--rocket { left: 1018px; top: 82px; width: 152px; height: 152px; }

  .edge-rule { position: absolute; left: 1195px; top: 160px; width: 2px; height: 200px; background: var(--ink); }
</style>
</head>
<body>
<main class="canvas">
  <div class="landscape" role="img" aria-label="Cloudy blue sky over distant mountains and a treeline, with a cracked dry lakebed in the foreground"></div>

  <div class="echo echo--vision" aria-hidden="true">VISION</div>
  <div class="echo echo--purpose" aria-hidden="true">PURPOSE</div>
  <div class="echo echo--mission" aria-hidden="true">MISSION</div>

  <svg class="icon icon--eye" viewBox="0 0 222 102" aria-hidden="true">
    <path d="M4 52 C50 6 130 -6 218 52 C130 106 50 100 4 52 Z" fill="none" stroke="#fff" stroke-width="5"/>
    <path d="M20 52 C60 18 125 10 196 52 C125 92 60 88 20 52 Z" fill="none" stroke="#fff" stroke-width="4"/>
    <circle cx="112" cy="52" r="36" fill="none" stroke="#fff" stroke-width="5"/>
    <circle cx="112" cy="52" r="22" fill="none" stroke="#fff" stroke-width="4"/>
    <circle cx="104" cy="42" r="6" fill="none" stroke="#fff" stroke-width="3"/>
  </svg>

  <svg class="icon icon--heart" viewBox="0 0 168 138" aria-hidden="true">
    <path d="M84 130 L18 68 C-4 46 6 8 40 6 C60 5 76 18 84 32 C92 18 108 5 128 6 C162 8 172 46 150 68 Z" fill="none" stroke="#fff" stroke-width="6" stroke-linejoin="round"/>
    <path d="M84 116 L26 62 C10 46 17 18 42 17 C60 16 74 30 84 46 C94 30 108 16 126 17 C151 18 158 46 142 62 Z" fill="none" stroke="var(--icon-fill)" stroke-width="9" stroke-linejoin="round"/>
  </svg>

  <svg class="icon icon--rocket" viewBox="0 0 152 152" aria-hidden="true">
    <g transform="rotate(-45 76 76)">
      <path d="M76 4 C100 28 106 60 100 100 L52 100 C46 60 52 28 76 4 Z" fill="var(--icon-fill)" stroke="#fff" stroke-width="3"/>
      <path d="M52 76 L30 112 L54 104 Z M100 76 L122 112 L98 104 Z" fill="var(--icon-fill)" stroke="#fff" stroke-width="3"/>
      <path d="M64 104 L76 140 L88 104 Z" fill="var(--icon-fill)" stroke="#fff" stroke-width="3"/>
      <circle cx="76" cy="48" r="10" fill="none" stroke="#fff" stroke-width="5"/>
    </g>
  </svg>

  <h2 class="title title--vision">VISION</h2>
  <h2 class="title title--purpose">PURPOSE</h2>
  <h2 class="title title--mission">MISSION</h2>

  <p class="statement statement--vision">We will exceed all expectations<br>and become the inspirational<br>driving force behind our<br>community's young leaders,<br>assisting them to create people<br>centric business cultures that<br>are known throughout the<br>country</p>

  <p class="statement statement--purpose">We exist, to empower the<br>talented to achieve the<br>extraordinary</p>

  <div class="statement statement--mission">
    <p>We will work hand in hand with local<br>business leaders to demonstrate the<br>values and benefits of a people centric<br>leadership philosophy. This influence<br>will usher in a new generation of young<br>leader that will ultimately contribute<br>and drive the future growth and<br>development of the community in which<br>they work.</p>
    <p>Through the expert delivery of our<br>services, we will help to create a world<br>where each and every person will know<br>their true personal &amp; professional<br>value, and who will embrace their<br>career with the same gusto and passion<br>as they do their life.</p>
    <p>We will achieve all of this; by having<br>the courage to say what we believe is<br>right, selflessly leading others for the<br>betterment of humankind, adapting and<br>overcoming each and every new<br>challenge, and by holding firm to our<br>belief that nothing is impossible.</p>
  </div>

  <div class="edge-rule" aria-hidden="true"></div>
</main>
</body>
</html>
```